Wine Company Flyer Design

Hello,

I need a flyer design that will fit an 11 inch width by 17 inch height. Design has to be submitted in PDF X-1a format.

We want our logo on the flyer with the slogan underneath it saying "Better Wines Lower Prices"

We want a nice design and then we will get to some of the text that will be on the flyer.

Please make the flyer in two colors ONLY. Use the colors of our logo for the rest of the design.

Requirements
Must have
• PDF x-1a format
• Logo on flyer with slogan "Better Wines Lower Prices" underneath
• Two colors - Orange, Red (Same as logo colors)
• Fits in an 11"x17" format for printing
• This will be for the wine industry so include elements of wine in the flyer and make it look nice. Leave some space in the middle of the design for text to be put in.

```html
<!DOCTYPE html>
<html lang="en">
<head>
<meta charset="utf-8">
<title>Vinovale Flyer</title>
<link href="https://fonts.googleapis.com/css2?family=Fredoka:wght@600&family=Ubuntu:wght@400;500&display=swap" rel="stylesheet">
<style>
  :root {
    --stage: #e9e6e2;
    --orange: #f0921e;
    --red: #e12228;
    --white: #ffffff;
    --ink-soft: rgba(255,255,255,0.94);
  }
  * { box-sizing: border-box; margin: 0; padding: 0; }
  html, body {
    width: 1200px; height: 800px; overflow: hidden;
    background: var(--stage);
  }
  .flyer {
    position: absolute;
    left: 354px; top: 20px;
    width: 492px; height: 760px;
    background: var(--orange);
    overflow: hidden;
    box-shadow: 0 6px 18px rgba(0,0,0,0.18);
  }
  .flyer__field {
    position: absolute; inset: 0;
    width: 100%; height: 100%;
  }
  .art {
    position: absolute;
    background: linear-gradient(180deg, #ffffff, #f7f3ee);
    border-radius: 18px;
  }
  .art--glass { left: 58px; top: 108px; width: 104px; height: 250px; }
  .art--bottle { left: 112px; top: 420px; width: 100px; height: 318px; }
  .brand {
    position: absolute;
    left: 215px; top: 62px;
    width: 260px;
    display: flex; flex-direction: column; align-items: center; gap: 10px;
  }
  .brand__dot {
    width: 58px; height: 58px; border-radius: 50%;
    background: var(--orange);
  }
  .brand__name {
    font-family: "Fredoka", sans-serif;
    font-weight: 600;
    font-size: 34px;
    letter-spacing: 1px;
    color: var(--white);
    line-height: 1;
  }
  .slogan {
    position: absolute;
    left: 222px; top: 200px;
    font-family: "Fredoka", sans-serif;
    font-weight: 600;
    font-size: 46px;
    line-height: 1.05;
    color: var(--white);
  }
  .copy {
    position: absolute;
    font-family: "Ubuntu", sans-serif;
    font-size: 12px;
    line-height: 17px;
    color: var(--ink-soft);
    text-align: justify;
    hyphens: auto;
  }
  .copy--intro { left: 228px; top: 326px; width: 242px; }
  .copy--body { left: 200px; top: 440px; width: 272px; text-align-last: center; }
  .copy__curve {
    float: left;
    width: 170px; height: 260px;
    shape-outside: polygon(0 0, 36px 0, 60px 75px, 94px 150px, 138px 225px, 162px 260px, 0 260px);
  }
  .web {
    position: absolute;
    right: 30px; bottom: 28px;
    font-family: "Ubuntu", sans-serif;
    font-weight: 500;
    font-size: 15px;
    letter-spacing: 0.5px;
    color: var(--white);
  }
</style>
</head>
<body>
  <main class="flyer">
    <svg class="flyer__field" viewBox="0 0 492 760" aria-hidden="true">
      <path d="M215 0 C170 250 185 520 400 760 L492 760 L492 0 Z" fill="var(--red)"/>
      <circle cx="86" cy="382" r="15" fill="var(--red)"/>
      <circle cx="70" cy="470" r="14" fill="var(--red)"/>
      <circle cx="236" cy="545" r="11" fill="var(--red)"/>
      <circle cx="262" cy="728" r="18" fill="var(--red)"/>
    </svg>

    <div class="art art--glass" role="img" aria-label="White silhouette of a wine glass with a small red flower on its rim"></div>
    <div class="art art--bottle" role="img" aria-label="White silhouette of an upright wine bottle"></div>

    <header class="brand">
      <span class="brand__dot"></span>
      <span class="brand__name">VINOVALE</span>
    </header>

    <h1 class="slogan">Better Wines<br>Lower Prices</h1>

    <p class="copy copy--intro">Lorem ipsum dolor sit amet, consectetur adipiscing elit. Integer mollis venenatis consectetur. Morbi tincidunt tempor mauris quis placerat. Fusce id arcu suscipit libero vestibulum vehicula. Aenean nec velit vulputate, efficitur justo.</p>

    <p class="copy copy--body"><span class="copy__curve"></span>Lorem ipsum dolor sit amet, consectetur adipiscing elit. Integer mollis venenatis consectetur. Morbi tincidunt tempor mauris quis placerat. Fusce id arcu suscipit libero vestibulum vehicula. Aenean nec velit vulputate, efficitur justo ullamcorper, scelerisque neque. Nullam rhoncus lorem at laoreet venenatis. In tempus, libero vitae dictum eleifend, odio eros vehicula urna, ut tincidunt arcu orci sit amet mi. Donec blandit elementum enim, ac commodo est sagittis et.</p>

    <footer class="web">www.vinovale.com</footer>
  </main>
</body>
</html>
```